Help Meadowlane Ledger create a brochure with great copy!

I would like a double sided 11"x17" brochure designed. It will be fold in half to form a book (like this: http://www.quickfolioprints.example/summer/cart1/images/uploads/11x17bro.jpg)

It will have 4 sides, front/back and inside left/inside right.

We are building intuitive software to help farmers make better farm finance decisions. It's important to note that every farm is unique and our team of advisors will be standing by to help users with the software and to help them with specific decisions for their operation.

Our software will have the following features which I want to be highlighted in the brochure.

1 - Field-by-Field Budget Tracker (Here you'll show the Inputs screen and the Applications screen). The Inputs section is where users will track their yearly input variable and overhead expenses (seed, fertilizer, chemical, crop insurance, repairs, fuel, drying, crop insurance, debt payments, and misc. expenses). The Applications section is where users will easily assign these expenses to each field they farm.

They will build their budget before the growing season and adjust that budget to actual during the growing season.

2 - Field-by-Field Profit and Loss Tracking (where you'll show the field-by-field P&L screenshot). Users will be able to track their budgets on a field-by-field basis both yearly and cumulatively. This will give them better insight into which fields are the most profitable for their farm or which are costing them money. If fields are costing them money over the long-term, they can either choose to improve the fields or drop them.

3 - Grain Marketing Plan Builder (include the Marketing Plan Screenshot). This is where users can build a time and profit-based grain marketing plan. Most users make grain marketing (when, where, and at what price to sell) based on gut feel and emotion. Our grain marketing plan builder allows farmers to build a structured grain marketing plan.

4 - Grain Contract Tracking (include Grain Contract tracking screenshot). This is where users can track their current grain sales and contracts. Contract types include cash sales, forward contracts, basis contracts, hedge-to-arrive contracts, futures hedges, and option strategies. Throughout the growing season, users will be able to quickly analyze how much grain they have contracted and how much they have available to market.

Other features include futures markets, cash markets, market news and commentary, what/if analysis tools, educational materials, and personalized recommendations.
__________________________

Today's farmer wears many hats. They are typically the CEO, the Director of HR, the CFO, the Agronomist and the Mechanic. Farm risk management and finance often get overlooked when they are a huge driver of farm profits and losses. Our software combined with our staff of advisors will become a partner in their farming operation ensuring that they can survive and thrive during today's tough farm economy.

Rather than making decisions guided by gut feel and emotion, our software allows farmers to professionalize their farm finance and risk management.

Being a great farm finance manager is no longer a trait of the most successful farms, its necessity of all farms.

Please include farm focused-pictures from Pixorama. Pictures of wheat or corn fields.

I would like you to add additional sales-focused copy.

Meadowlane Ledger's address is 2817 Belwyn Pkwy S, Fargo, ND 58102. Contact is Tom Walsey (tomw@cropledgerservices.example) and 701-555-0148.

Target Market(s)

Agriculture, Farmers

Font styles to use
Sans Serif

Colors
acd036
9bcb3b

Requirements
Must have
• Good copy. Highlight software features and personalize service from advisors

```html
<!DOCTYPE html>
<html lang="en">
<head>
<meta charset="utf-8">
<title>Meadowlane Ledger – Software Features</title>
<link href="https://fonts.googleapis.com/css2?family=Open+Sans:ital,wght@0,300;0,400;0,600;0,700;1,700&display=swap" rel="stylesheet">
<style>
  :root{
    --green:#acd036;
    --green-2:#9bcb3b;
    --ink:#2f3133;
    --muted:#6d7073;
    --sidebar:#3b3e42;
    --sidebar-line:#5a5e63;
    --paper:#ffffff;
    --backdrop:#dcdcd8;
    --line:#e4e6e8;
    --chart-red:#d4413b;
  }
  *{box-sizing:border-box;margin:0;padding:0}
  html,body{width:1200px;height:804px;overflow:hidden}
  body{background:var(--backdrop);font-family:"Open Sans",Arial,sans-serif;color:var(--ink);position:relative}
  .spread{position:absolute;left:40px;top:22px;width:1120px;height:760px;display:flex;box-shadow:0 6px 24px rgba(0,0,0,.18)}
  .page{position:relative;width:560px;height:760px;background:var(--paper);overflow:hidden}
  .page--left{box-shadow:inset -10px 0 14px -10px rgba(0,0,0,.18)}
  .page--right{box-shadow:inset 10px 0 14px -10px rgba(0,0,0,.18)}
  .top-band{position:absolute;left:0;top:0;width:560px;height:120px}
  .page-title{position:absolute;left:0;top:44px;width:560px;text-align:center;color:#fff;font-weight:300;font-size:23px;letter-spacing:.5px}
  .intro{position:absolute;left:40px;top:116px;width:480px;font-size:10.5px;line-height:1.4;color:var(--ink)}
  .field-photo{position:absolute;left:0;top:250px;width:560px;height:510px;
    background:linear-gradient(180deg,#4f97d2 0%,#8fc0e6 28%,#e2eef6 48%,#cfdcc0 60%,#6d9a3b 68%,#3f6e22 100%)}
  .budget-panel{position:absolute;left:24px;top:232px;width:480px;height:376px;background:var(--green);border-radius:14px}
  .budget-copy{position:absolute;left:40px;top:258px;width:166px;color:#fff}
  .budget-copy p{font-size:9.5px;line-height:1.38;margin-bottom:10px}
  .budget-copy h2{font-size:14px;font-weight:700;line-height:1.2;margin:4px 0 10px}
  .footer-url{position:absolute;left:0;bottom:10px;width:560px;text-align:center;font-size:9.5px;letter-spacing:.4px}
  .page--left .footer-url{color:#fff}
  .page--right .footer-url{color:var(--muted)}

  /* app screens */
  .app{position:absolute;background:#fff;display:flex;box-shadow:0 3px 10px rgba(0,0,0,.22);overflow:hidden}
  .app__side{width:19%;background:var(--sidebar);padding:5px 4px}
  .app__brand{display:flex;align-items:flex-start;gap:3px;color:#fff;font-size:5px;line-height:1.2;font-weight:600;margin-bottom:6px}
  .app__brand i{flex:none;width:5px;height:5px;border-radius:50%;background:var(--green);display:block}
  .app__nav{height:3px;background:var(--sidebar-line);border-radius:1px;margin:0 0 5px 2px}
  .app__nav.is-active{background:var(--green)}
  .app__main{flex:1;padding:5px 7px;min-width:0}
  .app__tabs{display:flex;gap:10px;font-size:6px;color:#9a9da0;border-bottom:1px solid var(--line);padding-bottom:3px;margin-bottom:5px}
  .app__tabs b{color:var(--ink)}
  .app__tabs .is-current{color:var(--green-2);font-weight:700}
  .cards{display:grid;grid-template-columns:repeat(3,1fr);gap:5px}
  .card{border:1px solid var(--line);padding:3px;font-size:4.5px;color:var(--muted)}
  .card b{display:block;color:var(--ink);font-size:5px;margin-bottom:2px}
  .row-line{height:2px;background:var(--line);margin:3px 0}
  .pl-table{width:100%;border-collapse:collapse;font-size:6px}
  .pl-table th{text-align:left;color:var(--ink);font-weight:700;padding:2px;border-bottom:1px solid var(--line)}
  .pl-table td{padding:2.5px 2px;color:var(--muted);border-bottom:1px solid var(--line)}
  .pl-table td:first-child{color:var(--ink);font-weight:600}
  .chart-title{font-size:5.5px;font-weight:700;text-align:center;margin-bottom:2px}

  /* feature boxes */
  .feature{position:absolute;border:1.5px solid var(--green);border-radius:14px;background:#fff}
  .feature h2{color:var(--green-2);font-size:14px;font-weight:700;font-style:italic}
  .feature p{font-size:9.5px;line-height:1.36;color:var(--ink)}
  .feature--pl{left:22px;top:108px;width:516px;height:250px}
  .feature--pl h2{position:absolute;left:0;top:12px;width:100%;text-align:center}
  .feature--pl p{position:absolute;left:20px;top:38px;width:476px}
  .feature--plan{left:30px;top:390px;width:508px;height:160px}
  .feature--plan h2{position:absolute;left:18px;top:14px}
  .feature--plan p{position:absolute;left:18px;top:40px;width:244px}
  .feature--contract{left:30px;top:562px;width:508px;height:170px}
  .feature--contract h2{position:absolute;left:262px;top:14px}
  .feature--contract p{position:absolute;left:262px;top:38px;width:232px}
</style>
</head>
<body>
<main class="spread">

  <!-- Inside left -->
  <section class="page page--left">
    <svg class="top-band" viewBox="0 0 560 120" preserveAspectRatio="none" aria-hidden="true">
      <path d="M0 0H560V112Q280 92 0 102Z" fill="var(--green)"/>
    </svg>
    <h1 class="page-title">SOFTWARE FEATURES</h1>
    <p class="intro">We are building intuitive software to help farmers make better farm finance decisions. It's important to note that every farm is unique and our team of advisors will be standing by to help users with the software and to help them with specific decisions for their operation.</p>

    <div class="field-photo" role="img" aria-label="Blue sky with clouds over long rows of a green crop field"></div>

    <div class="budget-panel"></div>
    <div class="budget-copy">
      <p>Our software will have the following features which I want to be highlighted in the brochure.</p>
      <h2>1 - Field-by-Field<br>Budget Tracker</h2>
      <p>The Inputs section is where users will track their yearly input variable and overhead expenses (seed, fertilizer, chemical, crop insurance, repairs, fuel, drying, crop insurance, debt payments, and misc. expenses). The Applications section is where users will easily assign these expenses to each field they farm.</p>
      <p>They will build their budget before the growing season and adjust that budget to actual during the growing season.</p>
    </div>

    <div class="app" style="left:214px;top:226px;width:300px;height:150px" role="group" aria-label="Applications screen">
      <div class="app__side">
        <div class="app__brand"><i></i>Meadowlane Ledger</div>
        <div class="app__nav"></div><div class="app__nav"></div><div class="app__nav"></div>
        <div class="app__nav is-active"></div><div class="app__nav"></div><div class="app__nav"></div>
        <div class="app__nav"></div><div class="app__nav"></div><div class="app__nav"></div><div class="app__nav"></div>
      </div>
      <div class="app__main">
        <div class="app__tabs"><b>YEAR</b><span>ARCHIVE</span><span>2014</span><span class="is-current">2015</span><span>2016</span><span>2017</span></div>
        <div class="cards">
          <div class="card"><b>Bull Butte</b>Crop<div class="row-line"></div>Yield<div class="row-line"></div>Land<div class="row-line"></div></div>
          <div class="card"><b>Maple</b>Crop<div class="row-line"></div>Yield<div class="row-line"></div>Land<div class="row-line"></div></div>
          <div class="card"><b>E Quarter</b>Crop<div class="row-line"></div>Yield<div class="row-line"></div>Land<div class="row-line"></div></div>
          <div class="card"><b>Fertilizer</b><div class="row-line"></div><div class="row-line"></div><div class="row-line"></div><div class="row-line"></div></div>
          <div class="card"><b>Fertilizer</b><div class="row-line"></div><div class="row-line"></div><div class="row-line"></div><div class="row-line"></div></div>
          <div class="card"><b>Fertilizer</b><div class="row-line"></div><div class="row-line"></div><div class="row-line"></div><div class="row-line"></div></div>
        </div>
      </div>
    </div>

    <div class="app" style="left:214px;top:386px;width:306px;height:200px" role="group" aria-label="Inputs screen">
      <div class="app__side">
        <div class="app__brand"><i></i>Meadowlane Ledger</div>
        <div class="app__nav"></div><div class="app__nav"></div><div class="app__nav is-active"></div>
        <div class="app__nav"></div><div class="app__nav"></div><div class="app__nav"></div>
        <div class="app__nav"></div><div class="app__nav"></div><div class="app__nav"></div><div class="app__nav"></div>
      </div>
      <div class="app__main">
        <div class="app__tabs"><b>YEAR</b><span>ARCHIVE</span><span>2014</span><span class="is-current">2015</span><span>2016</span><span>2017</span></div>
        <div class="card" style="margin-bottom:5px"><b>Fertilizer</b><div class="row-line"></div><div class="row-line"></div><div class="row-line"></div><div class="row-line"></div></div>
        <div class="card" style="margin-bottom:5px"><b>Seed</b><div class="row-line"></div><div class="row-line"></div><div class="row-line"></div></div>
        <div class="card"><b>Chemical</b><div class="row-line"></div></div>
      </div>
    </div>

    <p class="footer-url">www.cropledgerservices.example</p>
  </section>

  <!-- Inside right -->
  <section class="page page--right">
    <svg class="top-band" viewBox="0 0 560 120" preserveAspectRatio="none" aria-hidden="true">
      <path d="M0 0H560V92Q280 86 0 110Z" fill="var(--green)"/>
    </svg>
    <h1 class="page-title" style="top:36px">SOFTWARE FEATURES</h1>

    <article class="feature feature--pl">
      <h2>2 - Field-by-Field Profit and Loss Tracking</h2>
      <p>Users will be able to track their budgets on a field-by-field basis both yearly and cumulatively. This will give them better insight into which fields are the most profitable for their farm or which are costing them money. If fields are costing them money over the long-term, they can either choose to improve the fields or drop them.</p>
    </article>

    <div class="app" style="left:14px;top:222px;width:500px;height:140px" role="group" aria-label="Field-by-field profit and loss screen">
      <div class="app__side">
        <div class="app__brand"><i></i>Meadowlane Ledger</div>
        <div class="app__nav"></div><div class="app__nav"></div><div class="app__nav"></div>
        <div class="app__nav"></div><div class="app__nav is-active"></div><div class="app__nav"></div>
        <div class="app__nav"></div><div class="app__nav"></div><div class="app__nav"></div>
      </div>
      <div class="app__main">
        <div class="app__tabs"><b>YEAR</b><span>ARCHIVE</span><span>2014</span><span class="is-current">2015</span><span>2016</span><span>2017</span></div>
        <table class="pl-table">
          <tr><th>Field</th><th>Crop</th><th>Yield</th><th>Revenue</th><th>Expenses</th><th>Break Even</th></tr>
          <tr><td>Eagle</td><td>Corn</td><td>107,882</td><td>$451,528</td><td>$399,877</td><td>$3.70</td></tr>
          <tr><td>Mill East</td><td>Corn</td><td>53,575</td><td>$213,500</td><td>$190,368</td><td>$3.57</td></tr>
          <tr><td>North Half</td><td>Corn</td><td>23,250</td><td>$95,000</td><td>$76,051</td><td>$3.31</td></tr>
          <tr><td>South Half</td><td>Soybeans</td><td>6,975</td><td>$62,775</td><td>$54,011</td><td>$7.74</td></tr>
          <tr><td>E Quarter</td><td>Corn</td><td>36,000</td><td>$144,000</td><td>$138,880</td><td>$3.85</td></tr>
        </table>
      </div>
    </div>

    <article class="feature feature--plan">
      <h2>3 - Grain Marketing Plan Builder</h2>
      <p>This is where users can build a time and profit-based grain marketing plan. Most users make grain marketing (when, where, and at what price to sell) based on gut feel and emotion. Our grain marketing plan builder allows farmers to build a structured grain marketing plan.</p>
    </article>

    <div class="app" style="left:300px;top:378px;width:244px;height:136px" role="group" aria-label="Marketing plan screen">
      <div class="app__side">
        <div class="app__brand"><i></i>Meadowlane Ledger</div>
        <div class="app__nav"></div><div class="app__nav"></div><div class="app__nav"></div>
        <div class="app__nav"></div><div class="app__nav"></div><div class="app__nav is-active"></div>
        <div class="app__nav"></div><div class="app__nav"></div>
      </div>
      <div class="app__main">
        <div class="app__tabs"><b>YEAR</b><span>2014</span><span class="is-current">2015</span><span>2016</span></div>
        <div class="chart-title">2015 Corn Marketing Plan</div>
        <svg viewBox="0 0 200 90" width="100%" height="88" aria-hidden="true">
          <g stroke="var(--line)" stroke-width=".6"><line x1="0" y1="15" x2="200" y2="15"/><line x1="0" y1="35" x2="200" y2="35"/><line x1="0" y1="55" x2="200" y2="55"/><line x1="0" y1="75" x2="200" y2="75"/></g>
          <g fill="#d9dbdd"><rect x="60" y="10" width="4" height="65"/><rect x="110" y="10" width="4" height="65"/><rect x="150" y="10" width="4" height="65"/></g>
          <polyline fill="none" stroke="var(--chart-red)" stroke-width="1" points="0,50 8,46 14,52 20,44 28,48 34,40 40,46 48,42 56,50 64,44 72,48 80,40 88,46 96,42 104,47 112,38 118,44 126,41 134,48 142,36 150,18 156,40 164,44 172,38 180,48 190,50 200,52"/>
          <g fill="var(--green)"><circle cx="20" cy="30" r="2"/><circle cx="62" cy="25" r="2"/><circle cx="112" cy="22" r="2"/><circle cx="152" cy="20" r="2"/></g>
        </svg>
      </div>
    </div>

    <article class="feature feature--contract">
      <h2>4 - Grain Contract Tracking</h2>
      <p>This is where users can track their current grain sales and contracts. Contract types include cash sales, forward contracts, basis contracts, hedge-to-arrive contracts, futures hedges, and option strategies. Throughout the growing season, users will be able to quickly analyze how much grain they have contracted and how much they have available to market.</p>
    </article>

    <div class="app" style="left:20px;top:580px;width:230px;height:140px" role="group" aria-label="Grain contract tracking screen">
      <div class="app__side">
        <div class="app__brand"><i></i>Meadowlane Ledger</div>
        <div class="app__nav"></div><div class="app__nav"></div><div class="app__nav"></div>
        <div class="app__nav"></div><div class="app__nav"></div><div class="app__nav"></div>
        <div class="app__nav is-active"></div><div class="app__nav"></div>
      </div>
      <div class="app__main">
        <div class="app__tabs"><b>YEAR</b><span>2014</span><span class="is-current">2015</span><span>2016</span></div>
        <div class="chart-title">2015 Corn Marketing Plan</div>
        <svg viewBox="0 0 200 90" width="100%" height="90" aria-hidden="true">
          <g stroke="var(--line)" stroke-width=".6"><line x1="0" y1="15" x2="200" y2="15"/><line x1="0" y1="35" x2="200" y2="35"/><line x1="0" y1="55" x2="200" y2="55"/><line x1="0" y1="75" x2="200" y2="75"/></g>
          <g fill="#d9dbdd"><rect x="70" y="10" width="4" height="65"/><rect x="120" y="10" width="4" height="65"/><rect x="160" y="10" width="4" height="65"/></g>
          <polyline fill="none" stroke="var(--chart-red)" stroke-width="1" points="0,52 10,46 18,50 26,42 34,48 42,44 50,50 58,40 66,46 74,42 82,48 90,40 98,46 106,44 114,50 122,30 128,44 136,40 144,48 152,36 160,20 166,42 174,46 182,40 190,48 200,50"/>
          <g fill="var(--green)"><circle cx="22" cy="30" r="2"/><circle cx="72" cy="26" r="2"/><circle cx="122" cy="22" r="2"/><circle cx="162" cy="18" r="2"/></g>
        </svg>
      </div>
    </div>

    <p class="footer-url">www.cropledgerservices.example</p>
  </section>

</main>
</body>
</html>
```